Welcome Card

We are a privately owned waste removal company. We need a postcard designed to insert into a card that we send out to new customers. This card will list some of our company policies. Our company is known for having "the purplest trucks", so we must incorporate the color purple.

```html
<!DOCTYPE html>
<html lang="en">
<head>
<meta charset="utf-8">
<title>Summit Ridge Sanitation – Welcome Card</title>
<link rel="stylesheet" href="https://fonts.googleapis.com/css2?family=Delius&family=Source+Sans+3:wght@700&display=swap">
<style>
  :root {
    --backdrop: #2e2838;
    --paper: #ebe7df;
    --paper-edge: #d9d3c7;
    --purple: #3a2f6e;
    --purple-dark: #241c4a;
    --ink: #1c1a22;
    --ribbon-text: #ffffff;
    --hill: #cfc6ba;
  }
  * { box-sizing: border-box; margin: 0; padding: 0; }
  html, body {
    width: 900px; height: 1200px; overflow: hidden;
    background: var(--backdrop);
  }
  .card {
    position: absolute; left: 90px; top: 65px;
    width: 720px; height: 1070px;
    background: var(--paper);
    box-shadow: 0 10px 30px rgba(0,0,0,.45);
    overflow: hidden;
    font-family: "Delius", "Comic Sans MS", sans-serif;
    color: var(--purple);
  }
  .brand {
    position: absolute; top: 120px; left: 0; width: 100%;
    text-align: center;
  }
  .brand-name {
    display: inline-flex; align-items: center; gap: 12px;
    font-size: 34px; line-height: 1; color: var(--purple);
  }
  .brand-mark {
    width: 22px; height: 22px; border-radius: 50%;
    background: var(--purple);
  }
  .brand-rule {
    width: 230px; height: 3px; margin: 22px auto 0;
    background: var(--purple);
  }
  .tagline {
    position: absolute; top: 250px; left: 0; width: 100%;
    text-align: center;
    font-family: "Source Sans 3", "Arial", sans-serif;
    font-weight: 700; font-size: 22px; line-height: 1.15;
    letter-spacing: -0.3px;
  }
  .tagline .lead { color: var(--ink); }
  .tagline .accent { color: var(--purple); }
  .ribbon {
    position: absolute; left: 70px; top: 305px;
    width: 580px; height: 100px;
  }
  .ribbon-text {
    position: absolute; left: 140px; top: 318px; width: 440px;
    text-align: center; color: var(--ribbon-text);
    font-size: 19px; line-height: 1.3;
  }
  .policies {
    position: absolute; left: 120px; top: 430px; width: 490px;
    list-style: none;
    font-size: 15.5px; line-height: 1.35; text-align: justify;
  }
  .policies li {
    position: relative; margin-bottom: 17px;
  }
  .policies li::before {
    content: ""; position: absolute; left: -20px; top: 9px;
    width: 6px; height: 6px; border-radius: 50%;
    background: var(--purple-dark);
  }
  .policies .left { text-align: left; }
  .blank {
    display: inline-block; width: 175px;
    border-bottom: 1px solid var(--purple);
  }
  .hills {
    position: absolute; left: 0; bottom: 0; width: 100%; height: 260px;
    background: linear-gradient(to top, var(--hill), rgba(207,198,186,0));
  }
  .contact {
    position: absolute; left: 130px; top: 845px;
    font-size: 19px;
  }
  .social {
    position: absolute; left: 155px; top: 900px;
    display: flex; align-items: center; gap: 8px;
    font-size: 16px; color: var(--purple);
  }
  .social-mark {
    width: 16px; height: 16px; background: var(--purple);
  }
</style>
</head>
<body>
  <main class="card">
    <div class="hills" role="img" aria-label="Faint mountain silhouettes along the bottom of the card"></div>

    <header class="brand">
      <div class="brand-name"><span class="brand-mark"></span>Summit Ridge Sanitation</div>
      <div class="brand-rule"></div>
    </header>

    <p class="tagline">
      <span class="lead">Great price. Best service.</span><br>
      <span class="accent">Purplest trucks.</span>
    </p>

    <svg class="ribbon" viewBox="0 0 580 100" aria-hidden="true">
      <polygon points="0,30 75,30 75,88 0,88 28,59" fill="var(--purple)"/>
      <polygon points="505,30 580,30 552,59 580,88 505,88" fill="var(--purple)"/>
      <polygon points="75,88 120,88 120,98" fill="var(--purple-dark)"/>
      <polygon points="505,88 460,88 460,98" fill="var(--purple-dark)"/>
      <rect x="70" y="4" width="440" height="84" fill="var(--purple)" stroke="#fff" stroke-width="2"/>
    </svg>
    <p class="ribbon-text">Thank you for signing up for service with<br>Summit Ridge Sanitation.</p>

    <ul class="policies">
      <li>Please remember to have your trash out for pickup by 7AM on <span class="blank">&nbsp;</span>. We are only in your area once a week and cannot send a truck back if you missed our truck.</li>
      <li>We can provide removal of furniture, appliances, construction and remodel materials for an extra charge. Please call our office to make arrangements.</li>
      <li>Late fees are assessed to accounts that have not been paid within 25 days of billing. We charge a restart fee once a suspended account is restarted.</li>
      <li class="left">Not responsible for damage to trash cans.</li>
      <li class="left">Holiday Service - call our office for information on Holiday Schedules.</li>
      <li class="left">Sign up for our newsletter at<br>www.summitridgesanitation.com</li>
    </ul>

    <p class="contact">Any questions, please call our office at 555-0147!</p>

    <div class="social"><span class="social-mark"></span>FriendHub</div>
  </main>
</body>
</html>
```